Women's Empowerment & Prayer Brunch - Matching Poster, flyer and Postcard

We are a Christian Event & Travel Company and we are hosting our inaugural event on June 10, 2017. This event is a women's empowerment & prayer brunch aboard a private yacht leaving out of Larkspur Landing, Maryland. The event will cater to women who have a vision to start or have already embarked on the journey of starting or growing a business or ministry. The event calls for a matching poster, flyer and postcard design that give an elegant & exquisite feel with just the right breath of freshness. The colors should reflect our logo as this is our launch event. I have also included 2 photos of the Coralwind Heritage Village production (one of our sponsors) - Please include but do not make it take over the design - this is to advertise the door prize. The final design will portray the branding of the company (Christian, travel, events, elegance, professional), the branding of the event (elegant and luxurious) and the importance of this launch event.
Please include the following information:
Brightwell Event & Travel Group presents
Event name: Climbing the Hill: Trust, Service & Devotion.
Tag Line/Description: An Exquisite Women's Empowerment & Prayer Brunch.
Guest Speaker: Minister Harriet L. Dunmore (Photo included)
VP of TrustLine
Asst. Pastor & First Lady of Gilead Baptist Church
Special Guest Psalmist: Minister Tessa Holbrook (Photo Included)
Worship Director of Stonefield Community Church
Vocalist, Songwriter, Musician, and Clinician
Venue: Aboard the Regal Tide Yacht
Dock: Larkspur Landing
342 Marlow Court, Oxen Hill, MD 20712
Boarding 10:00am
Sailing Promptly at 10:30am
(Please be on time the yacht will not wait)
Date: Saturday June 10, 2017
Tickets: Early Bird US$75.00/person (ends May 15, 2017)
Regular Tickets US$95.99
Purchase Tickets at www.brightwellevent-travel.example/climbing-the-hill
SPACE IS LIMITED DUE TO YACHT CAPACITY
Grand Prize: Julian Ardent Purse
Door Prize: 2 Tickets to the Islander Coralwind Heritage Village
Other prizes for special ladies in attendance.
Ladies are asked to dress in Elegant White Ensemble
Corporate Sponsors:
The Coralwind Heritage Village (Logo included)
R. Lanning Photography (Logo included)
Special Thanks to our Individual Sponsors:
Mrs. G. Whitlow, Mr. K Prentice & Mr. S. Dorsey

Target Market(s)

Women, Business, Ministry, Christians, Middle to Upper Class

Industry/Entity Type

Events

Font styles to use
Serif
Script

Requirements
Must have
• Elegance, professional, vivid in color & font. be creative in Visual and FONT!
• Poster: 18" X 24"
• Flyer: one sided.
• ***** the final design chosen will have a cross referenced design of 1 flyer, 1 postcard 1 poster. This was included so you have a reference - Be creative!!!!!!
Nice to have
• Matching across all 3 designs (poster, flyer & postcard) but sized appropriately and just enough difference to play up the design and be appealing.
• I uploaded 3 example flyers to give you inspiration of the type of visuals I'm looking for. I removed my amateur sample because the designs were copying it instead of being creative.
Should not have
• Any thing inappropriate, alcohol oriented or sexual

```html
<!DOCTYPE html>
<html lang="en">
<head>
<meta charset="utf-8">
<title>Climbing the Hill – Women's Empowerment &amp; Prayer Brunch</title>
<link rel="stylesheet" href="https://fonts.googleapis.com/css2?family=Abril+Fatface&family=Kalam:wght@400&family=EB+Garamond:ital,wght@0,400;0,600;1,400&family=Libre+Baskerville:wght@400;700&family=Josefin+Sans:wght@400&display=swap">
<style>
  :root {
    --wine-deep: #2a0604;
    --wine: #7c1c0d;
    --wine-glow: #a8321a;
    --gold: #e5b52a;
    --gold-soft: #f0cb55;
    --cream: #f3e8d2;
    --teal: #2a8ea8;
    --teal-deep: #176a84;
    --ink: #0f2236;
    --white: #ffffff;
  }
  * { margin: 0; padding: 0; box-sizing: border-box; }
  html, body { width: 900px; height: 1200px; overflow: hidden; background: var(--wine-deep); }
  .poster { position: relative; width: 900px; height: 1200px; overflow: hidden; }
  .backdrop { position: absolute; inset: 0; }
  .line { position: absolute; left: 0; width: 900px; text-align: center; white-space: nowrap; }

  .ribbon-text {
    position: absolute; left: 4px; top: 46px; width: 150px; text-align: center;
    transform: rotate(-39deg); font-family: "Libre Baskerville", serif; font-weight: 700;
    font-size: 17px; color: var(--ink);
  }

  .brand-name {
    position: absolute; left: 0; width: 900px; top: 120px; text-align: center;
    font-family: "Kalam", cursive; font-size: 20px; color: var(--gold);
  }
  .presents { top: 164px; font-family: "Kalam", cursive; font-size: 26px; color: var(--gold); }
  .event-title {
    top: 188px; font-family: "Abril Fatface", serif; font-size: 64px; letter-spacing: 1px;
    color: var(--gold); text-shadow: 2px 3px 0 #3a0d05;
  }
  .event-values {
    top: 253px; left: 420px; width: 365px; text-align: right;
    font-family: "EB Garamond", serif; font-size: 22px; color: var(--gold-soft);
  }
  .tagline { font-family: "Kalam", cursive; font-size: 32px; color: var(--gold); }
  .tagline.one { top: 280px; }
  .tagline.two { top: 314px; }

  .venue { font-family: "EB Garamond", serif; font-style: italic; color: var(--gold-soft); }
  .venue.name { top: 386px; font-size: 28px; }
  .venue.dock { top: 430px; font-size: 19px; letter-spacing: 0.5px; }
  .venue.address { top: 463px; font-size: 19px; }
  .venue.board { top: 505px; font-size: 25px; }
  .venue.sail { top: 534px; font-size: 25px; }
  .venue.note { top: 564px; font-size: 22px; }
  .venue.date { top: 603px; font-size: 28px; }

  .caption {
    position: absolute; top: 538px; text-align: center;
    font-family: "Libre Baskerville", serif; font-size: 14px; line-height: 19.5px; color: var(--cream);
  }
  .caption strong { font-weight: 700; }
  .caption.speaker { left: 0; width: 244px; }
  .caption.psalmist { left: 655px; width: 245px; }

  .ticket { font-family: "EB Garamond", serif; font-style: italic; color: var(--ink); }
  .ticket.early { top: 688px; font-size: 30px; }
  .ticket.early-end { top: 722px; font-size: 16px; }
  .ticket.regular { top: 745px; font-size: 30px; }
  .ticket.purchase { top: 779px; font-size: 16px; font-style: normal; }
  .ticket.url { top: 800px; font-size: 17px; font-style: normal; }
  .ticket.limited { top: 828px; font-size: 14px; letter-spacing: 0.3px; }
  .ticket.prize { font-size: 20px; }
  .ticket.grand { top: 849px; }
  .ticket.door { top: 875px; }
  .ticket.other { top: 902px; }
  .ticket.dress { top: 930px; font-size: 21px; color: var(--white); }
  .ticket.on-sale { top: 959px; font-size: 21px; letter-spacing: 0.5px; }

  .sponsor-title {
    top: 998px; font-family: "Josefin Sans", sans-serif; font-size: 18px; letter-spacing: 2px; color: var(--ink);
  }
  .sponsor-card {
    position: absolute; top: 1028px; height: 78px; background: var(--white); border-radius: 5px;
    display: flex; align-items: center; justify-content: center; text-align: center; padding: 6px;
    font-family: "EB Garamond", serif; font-weight: 600; color: var(--ink); line-height: 1.15;
  }
  .sponsor-card.photo { left: 314px; width: 86px; font-size: 12px; }
  .sponsor-card.village { left: 408px; width: 174px; font-size: 17px; }
  .thanks { font-family: "EB Garamond", serif; font-style: italic; font-size: 24px; color: var(--ink); }
  .thanks.heading { top: 1114px; }
  .thanks.names { top: 1143px; }
</style>
</head>
<body>
<main class="poster">
  <svg class="backdrop" width="900" height="1200" viewBox="0 0 900 1200" aria-hidden="true">
    <defs>
      <radialGradient id="wineGlow" cx="50%" cy="30%" r="75%">
        <stop offset="0" stop-color="#a8321a"/>
        <stop offset="0.45" stop-color="#7c1c0d"/>
        <stop offset="1" stop-color="#2a0604"/>
      </radialGradient>
      <linearGradient id="centerShade" x1="0" y1="0" x2="0" y2="1">
        <stop offset="0" stop-color="#1a0302" stop-opacity="0.55"/>
        <stop offset="1" stop-color="#1a0302" stop-opacity="0.2"/>
      </linearGradient>
      <linearGradient id="sea" x1="0" y1="0" x2="0" y2="1">
        <stop offset="0" stop-color="#2f97b1"/>
        <stop offset="1" stop-color="#1d7891"/>
      </linearGradient>
      <linearGradient id="fireGlow" x1="0" y1="0" x2="0" y2="1">
        <stop offset="0" stop-color="#1c1208"/>
        <stop offset="0.6" stop-color="#6b3410"/>
        <stop offset="1" stop-color="#140c06"/>
      </linearGradient>
      <linearGradient id="danceTones" x1="0" y1="0" x2="0" y2="1">
        <stop offset="0" stop-color="#4a3a22"/>
        <stop offset="1" stop-color="#b9952f"/>
      </linearGradient>
      <linearGradient id="speakerTones" x1="0" y1="0" x2="0" y2="1">
        <stop offset="0" stop-color="#6a3a2c"/>
        <stop offset="1" stop-color="#b3241e"/>
      </linearGradient>
      <linearGradient id="psalmistTones" x1="0" y1="0" x2="0" y2="1">
        <stop offset="0" stop-color="#2b2c33"/>
        <stop offset="1" stop-color="#a89b90"/>
      </linearGradient>
    </defs>

    <rect width="900" height="1200" fill="url(#wineGlow)"/>
    <path d="M330 0 C 300 220, 250 380, 275 560 C 290 620, 320 660, 330 680 L 570 680 C 580 660, 610 620, 625 560 C 650 380, 600 220, 570 0 Z" fill="url(#centerShade)"/>

    <path d="M0 672 C 150 652, 260 676, 420 666 C 560 656, 690 676, 900 660 L 900 1200 L 0 1200 Z" fill="url(#sea)"/>

    <path d="M0 0 L 150 0 L 0 170 Z" fill="#1d8aa3"/>

    <circle cx="452" cy="68" r="46" fill="none" stroke="var(--gold)" stroke-width="2.5"/>

    <ellipse cx="118" cy="424" rx="84" ry="112" fill="#0a0202"/>
    <ellipse cx="118" cy="424" rx="80" ry="108" fill="url(#speakerTones)" role="img" aria-label="Portrait photo of guest speaker Minister Harriet L. Dunmore"/>
    <ellipse cx="773" cy="424" rx="84" ry="112" fill="#0a0202"/>
    <ellipse cx="773" cy="424" rx="80" ry="108" fill="url(#psalmistTones)" role="img" aria-label="Portrait photo of special guest psalmist Minister Tessa Holbrook"/>

    <rect x="22" y="707" width="215" height="140" rx="4" fill="url(#danceTones)" role="img" aria-label="Photo of dancers in grass skirts performing at the Coralwind Heritage Village"/>
    <rect x="664" y="707" width="216" height="141" rx="4" fill="url(#fireGlow)" role="img" aria-label="Photo of fire dancers spinning flaming rings at night"/>

    <rect x="192" y="994" width="520" height="186" rx="8" fill="#ffffff" fill-opacity="0.22"/>
  </svg>

  <div class="ribbon-text">Limited Tickets</div>

  <div class="brand-name">Brightwell Event &amp; Travel Group</div>
  <div class="line presents">Presents</div>
  <h1 class="line event-title">CLIMBING THE HILL</h1>
  <div class="line event-values">TRUST ~ SERVICE ~ DEVOTION</div>
  <div class="line tagline one">An Exquisite Women's Empowerment</div>
  <div class="line tagline two">&amp; Prayer Brunch</div>

  <div class="line venue name">Venue : Aboard the Regal Tide Yacht</div>
  <div class="line venue dock">DOCK : LARKSPUR LANDING</div>
  <div class="line venue address">342 Marlow Court, Oxen Hill, MD 20712</div>
  <div class="line venue board">Boarding: 10:00 am</div>
  <div class="line venue sail">Sailing Promptly at: 10:30 am</div>
  <div class="line venue note">(Please be on time the yacht will not wait)</div>
  <div class="line venue date">Saturday 10th June 2017</div>

  <p class="caption speaker">Guest Speaker<br><strong>Minister Harriet L. Dunmore</strong><br>VP of TrustLine<br>Asst. Pastor &amp; First Lady of<br>Gilead Baptist Church</p>
  <p class="caption psalmist">Special Guest Psalmist<br><strong>Minister Tessa Holbrook</strong><br>Worship Director of Stonefield<br>Community Church<br>Vocalist, Songwriter, Musician<br>and Clinician</p>

  <div class="line ticket early">Early Bird: $75 /Person</div>
  <div class="line ticket early-end">Early Birds ends 15th May 2017</div>
  <div class="line ticket regular">Regular Tickets: $95.99 /Person</div>
  <div class="line ticket purchase">Purchase Tickets at</div>
  <div class="line ticket url">www.brightwellevent-travel.example/climbing-the-hill</div>
  <div class="line ticket limited">SPACE IS LIMITED DUE TO YACHT CAPACITY</div>
  <div class="line ticket prize grand">Grand Prize: Julian Ardent Purse</div>
  <div class="line ticket prize door">Door Prize: 2 Tickets to the Islander Coralwind Heritage Village</div>
  <div class="line ticket prize other">Other prizes for special ladies in attendance</div>
  <div class="line ticket dress">Ladies are asked to dress in Elegant White Ensembles</div>
  <div class="line ticket on-sale">Tickets on Sale 18th March 2017</div>

  <div class="line sponsor-title">CORPORATE SPONSORS</div>
  <div class="sponsor-card photo">R. Lanning Photography</div>
  <div class="sponsor-card village">Coralwind Heritage Village</div>
  <div class="line thanks heading">Special Thanks to our Individual Sponsors</div>
  <div class="line thanks names">Mrs. G. Whitlow, Mr. K Prentice and Mr. S. Dorsey</div>
</main>
</body>
</html>
```